Business card design needed for Automotive Reconditioning business

I have a logo design i just cant decide on the best color or layout for the business card, I will upload all the files so you can see all colors schemes we are considering. I have other file formats if needed let me know.

Target Market(s)

automotive dealerships

Contact Information for Business Card

HERE are the Descriptions and info needed on the card:
Interior Repair: Leather carpet burns panels dash Deoderize
Dealer products and Vin Verify
( spot for name and cell number) My name is Norman Bexley phone 614 352-4180 Title COO www.QuorvalMotive.com

Font styles to use
Sans Serif
Other font styles liked:
• what ever you think looks best

Requirements
Must have
• Must be able to change the name and phone for employees

```html
<!DOCTYPE html>
<html lang="en">
<head>
<meta charset="utf-8">
<title>Quorval Motive – Business Card</title>
<link rel="stylesheet" href="https://fonts.googleapis.com/css2?family=Exo+2:wght@600;800&family=PT+Sans:wght@400;700&display=swap">
<style>
  :root {
    --stage: #1b1b1c;
    --card: #262424;
    --red: #e8432a;
    --blue: #1f8fd8;
    --blue-deep: #1d5fb6;
    --white: #f2f2f2;
    --grey: #d6d6d6;
  }
  * { margin: 0; padding: 0; box-sizing: border-box; }
  html, body {
    width: 1200px; height: 1200px; overflow: hidden;
    background: var(--stage);
  }
  .canvas {
    position: relative; width: 1200px; height: 1200px;
    display: flex; flex-direction: column; align-items: center;
    justify-content: center; gap: 50px;
  }
  .card {
    position: relative; width: 900px; height: 515px;
    background: var(--card); overflow: hidden;
    box-shadow: 0 18px 40px rgba(0,0,0,.55);
  }
  .card--back { border-radius: 0 60px 0 60px; }
  .card--front { border-radius: 60px 0 60px 0; }

  .brand {
    position: absolute; left: 0; right: 0;
    display: flex; flex-direction: column; align-items: center;
    font-family: "Exo 2", sans-serif; font-weight: 800;
    color: var(--red); text-transform: uppercase; text-align: center;
  }
  .brand__name { display: flex; align-items: center; gap: 18px; font-size: 64px; letter-spacing: 2px; line-height: 1; }
  .brand__mark { width: 26px; height: 26px; background: var(--red); }
  .brand__tag { font-size: 24px; letter-spacing: 3px; margin-top: 12px; }

  .card--back .brand { top: 170px; }
  .back__url {
    position: absolute; left: 0; right: 0; top: 390px; text-align: center;
    font-family: "PT Sans", sans-serif; font-weight: 700; font-size: 20px;
    color: var(--red); letter-spacing: 1px;
  }

  .card--front .brand { top: 80px; }
  .contact {
    position: absolute; left: 60px; top: 265px; width: 380px;
    text-align: right; font-family: "PT Sans", sans-serif;
  }
  .contact__name {
    font-family: "Exo 2", sans-serif; font-weight: 800; font-size: 33px;
    color: var(--white); text-transform: uppercase; letter-spacing: 1px;
  }
  .contact__title { color: var(--blue); }
  .contact__line {
    display: flex; justify-content: flex-end; align-items: center; gap: 12px;
    font-size: 24px; color: var(--grey); margin-top: 8px; letter-spacing: 1px;
  }
  .contact__line svg { width: 22px; height: 22px; flex: none; }
  .divider {
    position: absolute; left: 470px; top: 275px; width: 2px; height: 140px;
    background: var(--red);
  }
  .services {
    position: absolute; left: 500px; top: 268px;
    font-family: "PT Sans", sans-serif; color: var(--grey);
  }
  .services__heading {
    font-family: "Exo 2", sans-serif; font-weight: 800; font-size: 30px;
    color: var(--blue); text-transform: uppercase; letter-spacing: 1px;
  }
  .services__list { list-style: none; font-size: 26px; line-height: 1.2; letter-spacing: 1px; }
  .services__list li { display: flex; align-items: center; gap: 10px; }
  .services__list li::before {
    content: ""; width: 11px; height: 11px; border-radius: 50%; background: var(--red);
  }
  .services__extra { font-size: 26px; letter-spacing: 1px; margin-top: 2px; }
  .band {
    position: absolute; left: 0; right: 0; bottom: 0; height: 16px; display: flex;
  }
  .band__red { flex: 1; background: linear-gradient(90deg, var(--red), #d23a26); }
  .band__blue { flex: 1; background: linear-gradient(90deg, var(--blue-deep), var(--blue)); }
</style>
</head>
<body>
<main class="canvas">
  <section class="card card--back">
    <div class="brand">
      <div class="brand__name"><span class="brand__mark"></span>Quorval Motive</div>
      <div class="brand__tag">Reconditioning Corp.</div>
    </div>
    <p class="back__url">WWW.QUORVALMOTIVE.COM</p>
  </section>

  <section class="card card--front">
    <div class="brand">
      <div class="brand__name"><span class="brand__mark"></span>Quorval Motive</div>
      <div class="brand__tag">Reconditioning Corp.</div>
    </div>

    <div class="contact">
      <h1 class="contact__name">Norman Bexley <span class="contact__title">COO</span></h1>
      <p class="contact__line">614 352-4180
        <svg viewBox="0 0 24 24" aria-hidden="true"><path fill="#e8432a" d="M6.6 10.8a15 15 0 0 0 6.6 6.6l2.2-2.2a1 1 0 0 1 1-.25 11.4 11.4 0 0 0 3.6.57 1 1 0 0 1 1 1V20a1 1 0 0 1-1 1A17 17 0 0 1 3 4a1 1 0 0 1 1-1h3.5a1 1 0 0 1 1 1c0 1.25.2 2.45.57 3.57a1 1 0 0 1-.25 1z"/></svg>
      </p>
      <p class="contact__line">www.QuorvalMotive.com
        <svg viewBox="0 0 24 24" aria-hidden="true"><g fill="none" stroke="#e8432a" stroke-width="1.8"><circle cx="12" cy="12" r="9"/><ellipse cx="12" cy="12" rx="4" ry="9"/><path d="M3 12h18M5 7h14M5 17h14"/></g></svg>
      </p>
    </div>

    <div class="divider"></div>

    <div class="services">
      <h2 class="services__heading">Interior Repair</h2>
      <ul class="services__list">
        <li>Leather Carpet</li>
        <li>Burns Panels</li>
        <li>Dash Deoderize</li>
      </ul>
      <p class="services__extra">Dealer products and Vin Verify</p>
    </div>

    <div class="band"><span class="band__red"></span><span class="band__blue"></span></div>
  </section>
</main>
</body>
</html>
```